Wayline Billboard Co Business Card Design

We have a newly created business and logo, but we now need business cards using the new logo.
We are an Australian based business, and we sell advertising space on trucks. The business cards will be seen by media buyers, direct advertisers, fleet owners and business people in general.
Our colours are very simple - black and a strong yellow, with some white. We have chosen the black and yellow for various reasons, but in particular because they are high contrast, and they also have a parallel with the number plates used on our roads, which is relevant to our product offering.
My initial thoughts:
Keep it simple and uncluttered
Use both sides
Our default is Century Gothic
I can provide logo files as required. We do not yet have a website, so I can't direct you there just yet. That may well be another project!
Target Market(s)
The business cards will be seen by media buyers, direct advertisers, fleet owners and business people in general.
Industry/Entity Type
Advertising
Look and feel
Each slider illustrates characteristics of the customer's brand and the style your logo design should communicate.

```html
<!DOCTYPE html>
<html lang="en">
<head>
<meta charset="utf-8">
<title>Wayline Billboard Co Business Card</title>
<link href="https://fonts.googleapis.com/css2?family=Didact+Gothic&display=swap" rel="stylesheet">
<style>
  :root {
    --yellow: #f4ec1e;
    --ink: #231f20;
    --ink-soft: #4a4648;
    --stage: #e9e6e2;
    --white: #ffffff;
  }
  * { margin: 0; padding: 0; box-sizing: border-box; }
  html, body {
    width: 1200px; height: 994px; overflow: hidden;
    background: var(--stage);
    font-family: "Didact Gothic", "Century Gothic", sans-serif;
  }
  .sheet {
    width: 1200px; height: 994px;
    display: flex; flex-direction: column; align-items: center; justify-content: center;
    gap: 48px;
  }
  .card {
    width: 756px; height: 432px;
    position: relative;
    box-shadow: 0 6px 18px rgba(0,0,0,0.14);
  }
  .card-front { background: var(--yellow); color: var(--ink-soft); }
  .card-back {
    background: var(--ink);
    display: flex; align-items: center; justify-content: center;
  }

  .brand {
    position: absolute; left: 48px; top: 150px;
    display: flex; align-items: center; gap: 14px;
    color: var(--ink);
  }
  .brand-mark { width: 26px; height: 26px; background: var(--ink); }
  .brand-name { font-size: 26px; letter-spacing: 1px; line-height: 1.15; }

  .person { position: absolute; right: 46px; top: 60px; text-align: right; }
  .person-name { font-size: 34px; letter-spacing: 1.5px; color: var(--ink-soft); }
  .person-role { font-size: 17px; margin-top: 4px; color: var(--ink-soft); }

  .contact { position: absolute; left: 408px; top: 214px; width: 302px; font-size: 16px; }
  .contact-address { padding-bottom: 10px; border-bottom: 1px solid var(--ink-soft); }
  .contact-list { list-style: none; margin-top: 14px; }
  .contact-list li { display: flex; align-items: center; gap: 10px; line-height: 1.55; }
  .contact-list svg { width: 12px; height: 12px; fill: var(--ink); flex: none; }

  .back-brand { text-align: center; color: var(--yellow); }
  .back-brand-name { font-size: 64px; letter-spacing: 3px; line-height: 1.1; }
  .back-brand-sub { font-size: 22px; letter-spacing: 14px; margin-top: 18px; }
</style>
</head>
<body>
<main class="sheet">
  <section class="card card-front" aria-label="Card front">
    <div class="brand">
      <span class="brand-mark"></span>
      <span class="brand-name">WAYLINE<br>BILLBOARD CO</span>
    </div>
    <div class="person">
      <p class="person-name">DANIEL HARTLEY</p>
      <p class="person-role">Managing Director</p>
    </div>
    <div class="contact">
      <p class="contact-address">14/6 Marlow Street, Brookvale NSW 2100</p>
      <ul class="contact-list">
        <li><svg viewBox="0 0 12 12" aria-hidden="true"><path d="M2 1h2.5l1 3-1.5 1a7 7 0 0 0 3 3l1-1.5 3 1V10a1 1 0 0 1-1 1A9 9 0 0 1 1 2a1 1 0 0 1 1-1z"/></svg>(702) 555-0148 x101</li>
        <li><svg viewBox="0 0 12 12" aria-hidden="true"><rect x="3" y="1" width="6" height="4"/><rect x="1" y="5" width="10" height="5" rx="1"/><rect x="3" y="8" width="6" height="3" fill="#fff"/></svg>(702) 555-0172</li>
        <li><svg viewBox="0 0 12 12" aria-hidden="true"><path d="M1 3h10v7H1z"/><path d="M1 3l5 4 5-4" fill="none" stroke="#f4ec1e" stroke-width="1"/></svg>daniel@wayline.com.au</li>
        <li><svg viewBox="0 0 12 12" aria-hidden="true"><circle cx="6" cy="6" r="5"/><path d="M1 6h10M6 1v10M3 3.5h6M3 8.5h6" stroke="#f4ec1e" stroke-width="0.7" fill="none"/></svg>www.wayline.com.au</li>
      </ul>
    </div>
  </section>

  <section class="card card-back" aria-label="Card back">
    <div class="back-brand">
      <p class="back-brand-name">WAYLINE BILLBOARD CO</p>
      <p class="back-brand-sub">AUSTRALIA</p>
    </div>
  </section>
</main>
</body>
</html>
```